Bright Harbor Goods - Product Page

Looking for a design for our product pages to showcase all of the following information in an aesthetically pleasing way. <br/><br/>• Product price per piece & price breaks<br/>• Set up cost <br/>• Additional color cost<br/>• Imprint side <br/>• Product Dimensions<br/><br/>Attached are photos showing ideas we have come up with to display the information. <br/><br/>The link below shows how our product pages is currently laid out. <br/><br/>Link to webpage: https://www.brightharborgoods.example/non-woven-reusable-promo-totes.html<br/>

Number of Pages Required

1 page

Colors
33b8a4
33a6d7
3277b5
fece3e
f9a040
a3cd3a

Requirements
Must have
• • Product price per piece & price breaks
• • Set up cost
• • Additional color cost
• • Imprint side
• • Product Dimensions

```html
<!DOCTYPE html>
<html lang="en">
<head>
<meta charset="utf-8">
<title>Bright Harbor Goods – Non-Woven Reusable Promo Totes</title>
<link href="https://fonts.googleapis.com/css2?family=Fira+Sans:wght@400;500;600;700&family=Nunito+Sans:wght@400;600;700&display=swap" rel="stylesheet">
<style>
:root{
  --green:#5aad32;
  --navy:#0a4a6e;
  --orange:#ff4d00;
  --star:#f08a1c;
  --grey-bg:#f6f6f6;
  --panel:#f1f1f1;
  --text:#333;
  --teal:#33b8a4;--sky:#33a6d7;--blue:#3277b5;--yellow:#fece3e;--amber:#f9a040;--lime:#a3cd3a;
}
*{box-sizing:border-box;margin:0;padding:0}
html,body{width:674px;height:1200px;overflow:hidden;background:#fff}
body{position:relative;font-family:"Nunito Sans",sans-serif;color:var(--text)}
.abs{position:absolute}

/* header */
.site-header{left:0;top:0;width:674px;height:43px;background:#fff}
.brand{left:90px;top:11px;font:700 14px/1 "Fira Sans",sans-serif;color:var(--green);letter-spacing:.2px}
.rush{left:231px;top:7px;width:30px;height:30px;border-radius:50%;background:var(--orange);color:#fff;text-align:center;font:700 5px/1.1 "Fira Sans",sans-serif;padding-top:7px;box-shadow:0 1px 2px rgba(0,0,0,.3)}
.rush small{display:block;font-size:3px;margin-top:2px}
.call{left:296px;top:13px;width:80px;text-align:center;font-size:5px;color:#555}
.call strong{display:block;font:700 8px/1.2 "Fira Sans",sans-serif;color:var(--navy)}
.top-links{left:490px;top:4px;display:flex;gap:9px;font-size:4.5px;color:#555;white-space:nowrap}
.socials{left:538px;top:14px;display:flex;gap:6px}
.socials i{width:3.5px;height:3.5px;border-radius:50%;background:var(--navy);display:block}
.cart{left:414px;top:24px;display:flex;align-items:center;gap:2px}
.cart b{background:var(--green);color:#fff;font-size:4px;padding:0 2px;border-radius:1px}
.search{left:437px;top:22px;width:148px;height:12px;border:1px solid #ccc;font-size:4px;color:#888;padding:3px 4px}
.search svg{position:absolute;right:2px;top:2px}

.main-nav{left:0;top:43px;width:674px;height:17.5px;background:var(--green)}
.main-nav span{position:absolute;top:6px;transform:translateX(-50%);font:600 4.8px/1 "Fira Sans",sans-serif;color:#fff;white-space:nowrap}
.crumbs{left:0;top:60.5px;width:674px;height:13.5px;background:var(--navy);font-size:4.6px;color:#fff;padding:4px 0 0 89px}

/* product */
.product-zone{left:0;top:74px;width:674px;height:372px;background:var(--grey-bg)}
.gallery{left:108.5px;top:111px;width:248.5px;height:258px;background:#fff}
.swatch{top:102px;width:18px;height:18px;border-radius:50%}
.bag-photo{left:150px;top:140px;width:164px;height:186px;border-radius:12px 12px 6px 6px;background:linear-gradient(160deg,#2f5d2e,#1f4628)}
.thumb{top:358px;width:18px;height:22px;border-radius:3px 3px 2px 2px}
.thumb-active{left:212px;top:350px;width:38px;height:38px;border-radius:50%;background:#fff;box-shadow:0 1px 4px rgba(0,0,0,.2)}
.thumb-active div{position:absolute;left:11px;top:10px;width:16px;height:18px;border-radius:2px;background:#2f5d2e}

.p-title{left:376px;top:109px;width:200px;font:500 11px/14px "Fira Sans",sans-serif;letter-spacing:.8px;color:#333}
.p-title em{font-style:normal;color:var(--green)}
.desc-h{left:375px;top:143px;font:500 6.8px/1 "Fira Sans",sans-serif;color:#222}
.spec{left:376px;font-size:5.3px;color:#888}
.spec b{color:#222;font-weight:700}
.kf-h{left:376px;top:194px;font:500 6.8px/1 "Fira Sans",sans-serif;color:#222}
.features{left:382px;top:207px;list-style:none;font-size:4.6px;color:#777;line-height:9.85px}
.qty-l{left:376px;top:304px;font-size:4.8px;letter-spacing:.5px;color:#888}
.price-l{left:520px;top:304px;width:34px;text-align:right;font-size:5.5px;letter-spacing:.5px;color:#888}
.qty{left:376px;top:316px;width:40px;height:13px;background:#fff;box-shadow:0 1px 3px rgba(0,0,0,.2);display:flex;justify-content:space-around;align-items:center;font-size:7px}
.price{left:494px;top:317px;width:60px;text-align:right;font:700 9.5px/1 "Fira Sans",sans-serif;color:#222}
.btn{display:flex;align-items:center;justify-content:center;color:#fff;font:600 7px/1 "Fira Sans",sans-serif;border-radius:2px}
.buy{left:376px;top:344px;width:178px;height:18px;background:var(--green);letter-spacing:1.5px}
.sample{left:376px;top:373px;width:84px;height:18px;background:var(--orange)}
.quote{left:470.5px;top:373px;width:83.5px;height:18px;background:var(--navy)}

/* price tables */
.ptable{top:425px;width:228px;box-shadow:0 1px 4px rgba(0,0,0,.18);background:#fff}
.ptable h3{height:21px;color:#fff;font:600 7.5px/21px "Fira Sans",sans-serif;letter-spacing:.5px;text-align:center;border-radius:2px 2px 0 0}
.ptable table{width:100%;border-collapse:collapse;table-layout:fixed}
.ptable td{height:21px;text-align:center;font-size:5.3px;color:#666;border-right:1px solid #ddd;border-bottom:1px solid #ddd;letter-spacing:.3px}
.ptable td:last-child{border-right:0}
.ptable td.lab{font:600 6px "Fira Sans",sans-serif}
.stock h3{background:var(--navy)}.stock td.lab{color:var(--navy)}
.overseas h3{background:var(--orange)}.overseas td.lab{color:var(--orange)}

.charges{left:97px;top:497px;width:480px;display:flex;justify-content:space-between;font-size:5.3px;color:#666;letter-spacing:.2px}
.charges b{color:var(--navy);font:600 5.6px "Fira Sans",sans-serif}

/* tabs */
.tab{top:523.5px;height:21.5px;font:500 7.8px/21.5px "Fira Sans",sans-serif;text-align:center;letter-spacing:.5px;border-radius:3px 3px 0 0;background:#eee;color:var(--navy)}
.tab.on{background:var(--green);color:#fff;letter-spacing:1px}
.tab-line{left:97px;top:545px;width:480px;height:1px;background:var(--green)}
.review-zone{left:97px;top:546px;width:480px;height:226px;background:var(--panel);border-radius:0 0 3px 3px}
.reviews{left:107.6px;top:556px;width:263.4px;height:205px;background:#fff;box-shadow:0 1px 3px rgba(0,0,0,.12);overflow:hidden;border-radius:3px}
.reviews h4{height:21px;background:#7a7068;color:#fff;font:500 7.8px/21px "Fira Sans",sans-serif;padding-left:11px;letter-spacing:.4px}
.review{margin:0 10px;padding:6px 1px 5px;border-bottom:1px solid #ccc}
.review .by{font:400 7.8px/1 "Fira Sans",sans-serif;color:#666;letter-spacing:.3px;display:flex;align-items:center}
.review .by b{color:var(--navy);font-weight:600;margin-left:3px;width:48px}
.stars{color:var(--star);font-size:6px;letter-spacing:2px}
.stars s{color:#ccc;text-decoration:none}
.review p{margin-top:7px;font-size:5.8px;line-height:8.4px;color:#666}

.write-h{left:385px;top:554px;font:500 10.5px/1 "Fira Sans",sans-serif;color:#333;letter-spacing:.3px}
.reviewing{left:385px;top:572px;font:400 6px/9.2px "Fira Sans",sans-serif;color:#333;letter-spacing:.2px}
.reviewing span{color:var(--navy)}
.rate{left:386px;top:598.5px;width:179px;height:28px;background:#fff;border-radius:2px;box-shadow:0 1px 2px rgba(0,0,0,.1);display:flex;justify-content:center;gap:6px;align-items:center;font-size:18px;color:var(--star)}
.rate s{color:#ddd;text-decoration:none}
.lbl{left:386px;font-size:6.2px;color:#333}
.lbl i{color:#e02020;font-style:normal}
.field{left:386px;width:179px;background:#fff;border:1px solid #e0e0e0;font-size:6px;color:#888;padding:5px 7px;border-radius:2px}
.captcha{left:386px;top:737px;width:83.5px;height:24px;background:#f9f9f9;border:1px solid #ddd;border-radius:2px;font-size:4px;color:#555;display:flex;align-items:center;padding-left:7px;gap:4px}
.captcha .box{width:7px;height:7px;border:1px solid #aaa;background:#fff;border-radius:1px}
.captcha .mark{position:absolute;right:8px;top:5px;width:10px;height:10px;background:#c9d4e8;border-radius:2px}
.submit{left:484.5px;top:743.5px;width:80.5px;height:17.5px;background:var(--green);font-size:6.5px;font-weight:500}

/* recommended */
.rec-h{left:97px;top:829px;font:600 13px/1 "Fira Sans",sans-serif;color:#333;letter-spacing:.4px}
.view-all{left:514px;top:829px;width:55px;height:17px;background:var(--green);font-size:7px;font-weight:500;gap:4px}
.card{top:867px;width:109px;height:133.5px;background:#fff;box-shadow:0 0 4px rgba(0,0,0,.14);border-radius:2px;text-align:center}
.card .img{margin:6px auto 0;width:72px;height:68px;border-radius:4px}
.card p{font-size:5.8px;color:#555;line-height:11.6px}
.card p:first-of-type{margin-top:8px}
.card em{font-style:normal;color:var(--green)}
.card b{color:var(--navy)}
.card p.stars{color:var(--star);font-size:6.5px;letter-spacing:2.5px}
.card p.stars span{color:#666;letter-spacing:0;margin-left:3px;font-size:5.8px}
.arrow{top:925px;width:18px;height:18px;border-radius:50%;background:#fff;box-shadow:0 0 3px rgba(0,0,0,.3)}
.arrow svg{position:absolute;left:5px;top:4px}

/* footer */
.site-footer{left:0;top:1036.5px;width:674px;height:139.5px;background:linear-gradient(180deg,#22335a,#1a2c52)}
.f-brand{left:89px;top:1064px;font:700 12px/1 "Fira Sans",sans-serif;color:#fff}
.f-about{left:89px;top:1091px;width:118px;font-size:4.7px;line-height:7px;color:#e6e9f0}
.f-social{left:89px;top:1130px;display:flex;gap:5px}
.f-social i{display:block;width:3.5px;height:3.5px;border-radius:50%;background:#fff}
.f-col h5{font:500 6.6px/1 "Fira Sans",sans-serif;color:#fff;margin-bottom:8px;letter-spacing:.2px}
.f-col li{list-style:none;font-size:4.6px;line-height:9.85px;color:#fff;padding-left:3px}
.f-addr{font-size:4.6px;line-height:6.4px;color:#fff}
.f-rule{width:124px;height:1px;background:rgba(255,255,255,.2)}
.copy{left:0;top:1176px;width:674px;height:24px;background:var(--navy);text-align:center;font-size:4.6px;color:#fff;padding-top:11px}
.chat{left:608px;top:1174px;width:66px;height:26px;background:#7cc244;border-radius:13px 0 0 13px;color:#fff;font:600 4.6px/5.5px "Fira Sans",sans-serif;text-align:right;padding:7px 6px 0 0}
.chat i{position:absolute;left:1px;top:1px;width:24px;height:24px;border-radius:50%;background:#e7d9cf;border:1.5px solid #fff}
</style>
</head>
<body>

<header class="abs site-header">
  <div class="abs brand">Bright Harbor Goods</div>
  <div class="abs rush">FREE<br>RUSH<small>Click Here</small></div>
  <div class="abs call">Call Us Toll Free:<strong>1-800-555-0199</strong></div>
  <div class="abs top-links"><span>Home</span><span>About Us</span><span>Contact Us</span><span>Blog</span></div>
  <div class="abs socials"><i></i><i></i><i></i><i></i><i></i></div>
  <div class="abs cart">
    <svg width="6" height="5" viewBox="0 0 12 10"><path d="M0 1h2l2 6h6l2-5H3" fill="none" stroke="#222" stroke-width="1.6"/><circle cx="5" cy="9" r="1" fill="#222"/><circle cx="9" cy="9" r="1" fill="#222"/></svg>
    <b>0</b>
  </div>
  <div class="abs search">SEARCH ENTIRE STORE HERE...
    <svg width="7" height="7" viewBox="0 0 10 10"><circle cx="4" cy="4" r="3" fill="none" stroke="#5aad32" stroke-width="1.6"/><path d="M6.3 6.3 9 9" stroke="#5aad32" stroke-width="1.8"/></svg>
  </div>
</header>

<nav class="abs main-nav">
  <span style="left:210px">REUSABLE BAGS ▾</span>
  <span style="left:271px">SEED PAPER ▾</span>
  <span style="left:336px">REUSABLE BOTTLES ▾</span>
  <span style="left:400px">LANYARDS ▾</span>
  <span style="left:463px">ECO PROMO ITEMS ▾</span>
</nav>
<div class="abs crumbs">Home &nbsp;»&nbsp; <b>Non-Woven Reusable Promo Totes</b></div>

<section class="abs product-zone"></section>
<div class="abs gallery"></div>
<div class="abs swatch" style="left:158px;background:var(--teal)"></div>
<div class="abs swatch" style="left:184px;background:var(--sky)"></div>
<div class="abs swatch" style="left:210px;background:var(--blue)"></div>
<div class="abs swatch" style="left:237px;background:var(--yellow)"></div>
<div class="abs swatch" style="left:263px;background:var(--amber)"></div>
<div class="abs swatch" style="left:290px;background:var(--lime)"></div>
<div class="abs bag-photo" role="img" aria-label="Product photo: dark green tote bag with two handles"></div>

<div class="abs thumb" role="img" aria-label="Brown tote thumbnail" style="left:153px;background:#6b3a22"></div>
<svg class="abs" style="left:186px;top:364px" width="7" height="11" viewBox="0 0 7 11"><path d="M6 1 1.5 5.5 6 10" fill="none" stroke="#111" stroke-width="1.6"/></svg>
<div class="abs thumb-active"><div role="img" aria-label="Green tote thumbnail"></div></div>
<svg class="abs" style="left:266px;top:364px" width="7" height="11" viewBox="0 0 7 11"><path d="M1 1l4.5 4.5L1 10" fill="none" stroke="#111" stroke-width="1.6"/></svg>
<div class="abs thumb" role="img" aria-label="Pink tote thumbnail" style="left:294px;background:#b0506b"></div>

<h1 class="abs p-title">Non-Woven Reusable Promo Totes (SKU: <em>PP2</em>)</h1>
<div class="abs desc-h">DESCRIPTION</div>
<div class="abs spec" style="top:156px"><b>Size -</b> 13" W x 14" H x 7" D</div>
<div class="abs spec" style="top:167px"><b>Thickness -</b> 100 GSM</div>
<div class="abs spec" style="top:178px"><b>Imprint Area -</b> 8" W x 8" H</div>
<div class="abs kf-h">Key Features</div>
<ul class="abs features">
  <li>01. Spacious Main Compartment, 1274 Cubic Inches</li>
  <li>02. 22" Carry Straps</li>
  <li>03. Made from 100 GSM Non-Woven Polypropylene</li>
  <li>04. Eco-Friendly and 100% Recyclable</li>
  <li>05. Removable Hard Bottom Insert at the Base</li>
  <li>06. 5 Day Standard Production / RUSH service available</li>
  <li>07. 10 Day Production for Full Color Artwork</li>
  <li>08. 8" Wide x 8" High Imprint Area</li>
  <li>09. Made From Recycled Content</li>
</ul>
<div class="abs qty-l">QUANTITY</div>
<div class="abs price-l">PRICE</div>
<div class="abs qty"><span>-</span><span style="font-size:8px">1</span><span>+</span></div>
<div class="abs price">$ 132.99</div>
<div class="abs btn buy">BUY NOW</div>
<div class="abs btn sample">Order Free Sample</div>
<div class="abs btn quote">Request A Quote</div>

<div class="abs ptable stock" style="left:97px">
  <h3>In Stock</h3>
  <table>
    <tr><td class="lab">Qty</td><td>1</td><td>100+</td><td>250+</td><td>500+</td><td>1000+</td><td>2,500+</td><td>5,000+</td></tr>
    <tr><td class="lab">Price</td><td>$0.69</td><td>$1.46</td><td>$1.35</td><td>$1.30</td><td>$1.26</td><td>$1.23</td><td>$1.19</td></tr>
  </table>
</div>
<div class="abs ptable overseas" style="left:348.5px">
  <h3>Overseas</h3>
  <table>
    <tr><td class="lab">Qty</td><td>1</td><td>1000+</td><td>3,000+</td><td>5,000+</td><td>10,000+</td><td>25,000+</td><td>50,000+</td></tr>
    <tr><td class="lab">Price</td><td>$0.69</td><td>$1.14</td><td>$0.94</td><td>$0.89</td><td>$0.84</td><td>$0.74</td><td>$0.69</td></tr>
  </table>
</div>
<div class="abs charges">
  <span><b>Setup Cost:</b> $45.00 per color</span>
  <span><b>Additional Color:</b> $0.15 per piece</span>
  <span><b>Imprint Side:</b> Front (1 side) / Back +$0.20</span>
</div>

<div class="abs tab on" style="left:97px;width:105px">REVIEWS</div>
<div class="abs tab" style="left:203px;width:104px">Additional Info</div>
<div class="abs tab" style="left:308px;width:105px">Shipping Estimator</div>
<div class="abs tab-line"></div>
<section class="abs review-zone"></section>

<div class="abs reviews">
  <h4>Customer Reviews (38)</h4>
  <div class="review">
    <div class="by">Review by <b>Mark T</b><span class="stars">★★★★<s>★</s></span></div>
    <p>I was able to use this promotional tote bag to promote my business just the way I had planned. Very cost effective and they met my deadline with ease.</p>
  </div>
  <div class="review">
    <div class="by">Review by <b>Owen B</b><span class="stars">★★★★★</span></div>
    <p>These bags were a big time hit at my annual convention. Our logo really stood out nicely on the center of these eco-friendly bags. The cost fit within our budget. Great company to work with.</p>
  </div>
  <div class="review">
    <div class="by">Review by <b>Leo R</b><span class="stars">★★★★★</span></div>
    <p>Great product. I really am amazed and impressed with this company. They were very patient when assisting me find this item.</p>
  </div>
  <div class="review" style="border:0">
    <div class="by">Review by <b>Sam P</b><span class="stars">★★★★★</span></div>
    <p>Great product. I really am amazed and impressed with this company. They were very patient when assisting me find this item.</p>
  </div>
</div>

<h2 class="abs write-h">Write Your Own Review</h2>
<div class="abs reviewing">You're reviewing: <span>Non-Woven Reusable Promo Totes</span><br>How do you rate this product?</div>
<div class="abs rate">★★★★<s>★</s></div>
<div class="abs lbl" style="top:636px">Your Name<i>*</i></div>
<div class="abs field" style="top:646px;height:18px">Enter Your Name</div>
<div class="abs lbl" style="top:673px">Your Review<i>*</i></div>
<div class="abs field" style="top:683px;height:42px">Type your review here</div>
<div class="abs captcha"><span class="box"></span>I'm not a robot<span class="mark"></span></div>
<div class="abs btn submit">SUBMIT NOW</div>

<h2 class="abs rec-h">Recommended Products</h2>
<div class="abs btn view-all">View All
  <svg width="4" height="7" viewBox="0 0 4 7"><path d="M.5.5 3 3.5.5 6.5" fill="none" stroke="#fff" stroke-width="1"/></svg>
</div>
<div class="abs arrow" style="left:76px"><svg width="8" height="10" viewBox="0 0 8 10"><path d="M6 1 2 5l4 4" fill="none" stroke="#333" stroke-width="1.2"/></svg></div>
<div class="abs arrow" style="left:580px"><svg width="8" height="10" viewBox="0 0 8 10"><path d="M2 1l4 4-4 4" fill="none" stroke="#333" stroke-width="1.2"/></svg></div>

<div class="abs card" style="left:104px">
  <div class="img" role="img" aria-label="Product photo: green and red printed tote bags" style="background:linear-gradient(90deg,#3fbf4a 50%,#e8453c 50%)"></div>
  <p><em>Size :</em> 13" W x 15" H x 10" D</p><p><em>As Low As :</em> <b>$0.74</b></p><p><em>SKU :</em> PP3A</p>
  <p class="stars">★★★★★<span>23 Reviews</span></p>
</div>
<div class="abs card" style="left:223.6px">
  <div class="img" role="img" aria-label="Product photo: purple and beige printed tote bags" style="background:linear-gradient(90deg,#7650b8 50%,#e8d6b6 50%)"></div>
  <p><em>Size :</em> 13" W x 15" H x 10" D</p><p><em>As Low As :</em> <b>$0.74</b></p><p><em>SKU :</em> PP3A</p>
  <p class="stars">★★★★★<span>23 Reviews</span></p>
</div>
<div class="abs card" style="left:342.4px">
  <div class="img" role="img" aria-label="Product photo: green and tan printed tote bags" style="background:linear-gradient(90deg,#2aa84a 50%,#d9c5a5 50%)"></div>
  <p><em>Size :</em> 13" W x 15" H x 10" D</p><p><em>As Low As :</em> <b>$0.74</b></p><p><em>SKU :</em> PP3A</p>
  <p class="stars">★★★★★<span>23 Reviews</span></p>
</div>
<div class="abs card" style="left:461.3px">
  <div class="img" role="img" aria-label="Product photo: blue and red printed tote bags" style="background:linear-gradient(90deg,#1f68b5 50%,#d92d2d 50%)"></div>
  <p><em>Size :</em> 13" W x 15" H x 10" D</p><p><em>As Low As :</em> <b>$0.74</b></p><p><em>SKU :</em> PP3A</p>
  <p class="stars">★★★★★<span>23 Reviews</span></p>
</div>

<footer class="abs site-footer"></footer>
<div class="abs f-brand">Bright Harbor Goods</div>
<p class="abs f-about">Bright Harbor Goods is an eco-friendly company that specializes in manufacturing custom bags. BHG was founded in 2009 and has strived to make the world a better place ever since.</p>
<div class="abs f-social"><i></i><i></i><i></i><i></i><i></i></div>
<div class="abs f-col" style="left:215.5px;top:1060px">
  <h5>USEFUL LINKS</h5>
  <ul><li>Customer Service</li><li>Our Story</li><li>Site Map</li><li>FTC Disclosure</li><li>Privacy Policy</li><li>Contact Us</li><li>Art &amp; Imprint Policy</li><li>Free Rush</li></ul>
</div>
<div class="abs f-col" style="left:341.5px;top:1060px">
  <h5>WHY BUY FROM US</h5>
  <ul><li>Reusable Bag Stats</li><li>Best Price Guarantee</li><li>Return &amp; Refund Policy</li><li>Shipping Policy</li><li>In-Stock &amp; Custom Production</li><li>Frequently Asked Questions</li></ul>
</div>
<div class="abs f-col" style="left:468px;top:1060px">
  <h5>ADDRESS</h5>
  <p class="f-addr">410 Harbor Way, Suite 8<br>Portside, FL 30001</p>
  <div class="f-rule" style="margin:6px 0 5px"></div>
  <p class="f-addr">Phone: 1-800-555-0199</p>
  <div class="f-rule" style="margin:6px 0 5px"></div>
  <p class="f-addr">Email: info@brightharborgoods.example</p>
  <div class="f-rule" style="margin-top:6px"></div>
</div>
<div class="abs copy">© 2020 BrightHarborGoods.example</div>
<div class="abs chat"><i role="img" aria-label="Support agent portrait"></i>LEAVE<br>A MESSAGE</div>

</body>
</html>
```